i need a business card design for my family investment company "norvane holdings" based in dubai. its a diverse investment firm focusing on education, hospitality and automotive. the design has to be modern and try to incorporate the logo "E" in the design. details on card as follow

Tariq H Bin Rashoud
Managing Director
tariq@norvane.ae
www.norvane.ae

Harbor park,palmcrest tower, office 1730, dubai
tel. 04 3819025
mobile.050 4172958

Target Market(s)

card used for networking events and investor meetings

Industry/Entity Type

Hospitality

```html
<!DOCTYPE html>
<html lang="en">
<head>
<meta charset="utf-8">
<title>Norvane Holdings – Business Card</title>
<link rel="stylesheet" href="https://fonts.googleapis.com/css2?family=Source+Sans+3:wght@300;400;600&display=swap">
<style>
  :root {
    --backdrop: #2e2e2e;
    --card: #ffffff;
    --brand-blue: #44698f;
    --ink: #1c1c1c;
    --rule: #9fb0c2;
  }
  * { box-sizing: border-box; margin: 0; padding: 0; }
  html, body { width: 1200px; height: 1067px; overflow: hidden; }
  body {
    background: var(--backdrop);
    font-family: "Source Sans 3", "Helvetica Neue", Arial, sans-serif;
    position: relative;
  }
  .card {
    position: absolute;
    width: 533px;
    height: 333px;
    background: var(--card);
    overflow: hidden;
  }
  /* Front side */
  .card-front { left: 200px; top: 130px; }
  .front-tab {
    position: absolute; left: -6px; top: 22px;
    width: 16px; height: 62px;
    background: var(--brand-blue); border-radius: 5px;
  }
  .front-wordmark {
    position: absolute; left: 0; right: 0; top: 128px;
    text-align: center;
    font-weight: 300; font-size: 44px; letter-spacing: 9px;
    color: var(--ink); text-transform: uppercase;
  }
  .front-web {
    position: absolute; right: 40px; bottom: -8px;
    width: 140px; height: 44px; padding-top: 7px;
    background: var(--brand-blue); border-radius: 7px;
    color: #fff; font-size: 17px; text-align: center;
  }
  /* Back side */
  .card-back { left: 450px; top: 540px; }
  .contact-list {
    position: absolute; left: 38px; top: 68px;
    list-style: none;
  }
  .contact-item {
    display: flex; align-items: flex-start;
    color: var(--brand-blue); font-size: 16px; line-height: 22px;
    margin-bottom: 13px;
  }
  .contact-icon {
    flex: none; width: 19px; height: 19px; margin: 2px 8px 0 0;
    background: var(--brand-blue); border-radius: 4px;
  }
  .divider {
    position: absolute; left: 268px; top: 65px;
    width: 1px; height: 196px; background: var(--rule);
  }
  .back-wordmark {
    position: absolute; left: 285px; width: 230px; top: 110px;
    text-align: center;
    font-weight: 300; font-size: 24px; letter-spacing: 4px;
    color: var(--ink); text-transform: uppercase;
  }
  .holder-name {
    position: absolute; left: 285px; width: 230px; top: 214px;
    text-align: center; color: var(--brand-blue); font-size: 16px;
  }
  .holder-title {
    position: absolute; right: 26px; top: 238px;
    color: var(--ink); font-size: 11px; font-weight: 600;
  }
</style>
</head>
<body>
  <section class="card card-front" aria-label="Card front">
    <div class="front-tab"></div>
    <div class="front-wordmark">Norvane Holdings</div>
    <div class="front-web">www.norvane.ae</div>
  </section>

  <section class="card card-back" aria-label="Card back">
    <ul class="contact-list">
      <li class="contact-item">
        <svg class="contact-icon" viewBox="0 0 19 19" aria-hidden="true"><rect x="6.5" y="3.5" width="6" height="12" rx="1" fill="none" stroke="#fff" stroke-width="1.3"/><circle cx="9.5" cy="13.3" r=".7" fill="#fff"/></svg>
        <span>050 4172958</span>
      </li>
      <li class="contact-item">
        <svg class="contact-icon" viewBox="0 0 19 19" aria-hidden="true"><path d="M4 8c0-2 2.5-3 5.5-3s5.5 1 5.5 3h-2.5v-1h-6v1z" fill="#fff"/><rect x="5" y="9" width="9" height="5" rx="1" fill="#fff"/></svg>
        <span>04 3819025</span>
      </li>
      <li class="contact-item">
        <svg class="contact-icon" viewBox="0 0 19 19" aria-hidden="true"><rect x="4" y="5.5" width="11" height="8" fill="none" stroke="#fff" stroke-width="1.2"/><path d="M4 5.5l5.5 4.5 5.5-4.5" fill="none" stroke="#fff" stroke-width="1.2"/></svg>
        <span>tariq@norvane.ae</span>
      </li>
      <li class="contact-item">
        <svg class="contact-icon" viewBox="0 0 19 19" aria-hidden="true"><circle cx="9.5" cy="9.5" r="5" fill="none" stroke="#fff" stroke-width="1.2"/><ellipse cx="9.5" cy="9.5" rx="2" ry="5" fill="none" stroke="#fff" stroke-width="1"/><path d="M4.5 9.5h10" stroke="#fff" stroke-width="1"/></svg>
        <span>www.norvane.ae</span>
      </li>
      <li class="contact-item">
        <svg class="contact-icon" viewBox="0 0 19 19" aria-hidden="true"><path d="M9.5 3.5c-2.5 0-4 1.8-4 3.8 0 2.8 4 7.7 4 7.7s4-4.9 4-7.7c0-2-1.5-3.8-4-3.8z" fill="#fff"/><circle cx="9.5" cy="7.4" r="1.4" fill="#44698f"/></svg>
        <span>Harbor park,palmcrest tower,<br>office 1730, dubai.</span>
      </li>
    </ul>
    <div class="divider"></div>
    <div class="back-wordmark">Norvane Holdings</div>
    <div class="holder-name">Tariq H Bin Rashoud</div>
    <div class="holder-title">Managing Director</div>
  </section>
</body>
</html>
```